Brindle Tavern & Lodge Supplies need a website

We need a website designed and created to facilitate us to promote & sell our products online. We buy excess / clearance lots of pub, cafe, restaurant & hotel furniture and equipment (usually from businesses that have excess inventory after a refurb or have closed down). We then sell these to other businesses mainly through our Chatterly page "Brindle Tavern & Lodge Supplies" but the process is cumbersome for the following reasons:
1) We dont have a stock list and images as it changes daily and people can only rely on recent posts and dont know if something is for sale still or is sold
2) we do not have the facility to sell online.

We are open to ideas and design concepts

We already have a logo & stationery deisgned

its probably best to look through our Chatterly page to better understand what we do

We would consider a catalogue / by department / category user interface such as:
https://brambleworth-trade-fittings.co.uk/

Our preference would be to change / delete / update stock via smartphone to best facilitate the maintenance of the website which i will do myself

Suggested categories would include:
Bar Furniture
Bar Equipment
Restaurant Furniture
Catering Equipment
Bedroom Furniture
Miscellaneous

Sub categories would include:
Bar Furniture:
Bar Stools
Bar Tables
Benches
Tub chairs
Arm chairs
Pub Mirrors
Pub Signs
Pub Memorabilia

Bar Equipment:
Bottle Coolers
Ice Machines
Glass Washers
Tills
Lighting
Sound
Wireless waiter
Glassware
Taps
Line coolers
Snooker tables
Pool tables
gaming machines

Restaurant Furniture:
Tables
Chairs
Wine racks
Dressers
Couches
Bench seating
Tub Chairs
Arm chairs
High chairs
Menu boards
Mirrors
Pictures

Catering Equipment:
Fridges
Freezers
Ovens
Cookers
Fryers
Carvery units
Hot display units
Refrigerated displays
Sinks
Stainless steel units
Microwaves
Mixers
Crockery
Cutlery
Utensils
Glassware

Bedroom Furniture:
Beds
Headboards
Wardrobes
Lockers
Dressing Tables
Mirrors
Lamps
Pictures

Profit sharing schemes:
Pool Tables
Juke Boxes
Gaming Machines

Target Market(s)

Pubs
Restaurants
cafes
guest houses
hotels

Industry/Entity Type

Hospitality

Number of Pages Required

5+ page

Colors

Designer to choose colors to be used in the design.

Requirements
Must have
• Website featuring our categories of stock to sell
Nice to have
• Ecommerce option
Should not have
• just a front page

```html
<!DOCTYPE html>
<html lang="en">
<head>
<meta charset="utf-8">
<title>Brindle Tavern &amp; Lodge Supplies – 2m Mobile Bar</title>
<link rel="stylesheet" href="https://fonts.googleapis.com/css2?family=Source+Sans+3:wght@400;600;700&display=swap">
<style>
:root{
  --page:#f8f8f8;
  --white:#ffffff;
  --red:#b30c14;
  --brick:#b0333a;
  --orange:#e68a00;
  --cream:#fcf0dc;
  --ink:#333333;
  --muted:#555555;
  --link:#1a5dbf;
  --cyan:#1a9ad6;
  --line:#d9d9d9;
  --icon:#d2d2d2;
}
*{box-sizing:border-box;margin:0;padding:0}
html,body{width:1200px;height:998px;overflow:hidden}
body{background:var(--page);font-family:"Source Sans 3",sans-serif;color:var(--ink);position:relative}
.abs{position:absolute}

.dept-nav .dept{position:absolute;top:62px;width:171px;height:32px;border:2px solid var(--line);background:var(--white);
  font-size:14px;font-weight:600;letter-spacing:.3px;display:flex;align-items:center;justify-content:center;color:#333}
.dept-nav .dept.active{background:var(--red);border-color:var(--red);color:#fff}

.product-panel{position:absolute;left:146px;top:121px;width:911px;height:509px;background:var(--white);box-shadow:0 1px 4px rgba(0,0,0,.12)}

.sub-nav .sub{position:absolute;top:146px;height:28px;width:108px;background:var(--cream);font-size:11.5px;font-weight:600;
  display:flex;align-items:center;justify-content:center;color:#333}
.sub-nav .sub.active{background:var(--red);color:#fff;width:53px}

.thumb{position:absolute;left:164px;width:53px;height:50px;background:var(--white);border:1px solid #e2e2e2;padding:4px}
.thumb.current{border-color:#3a8a1a}
.thumb span{display:block;width:100%;height:100%;background:linear-gradient(120deg,#3a2a24 0%,#f0523a 45%,#e4402c 70%,#2a1c18 100%)}
.gallery-frame{position:absolute;left:217px;top:214px;width:362px;height:359px;border:1px solid #e2e2e2;background:var(--white)}
.gallery-photo{position:absolute;left:230px;top:234px;width:336px;height:323px;
  background:radial-gradient(ellipse at 45% 45%,#ff6a4a 0%,#e6402c 40%,#7a1c18 75%,#3a1412 100%)}

.title{left:599px;top:211px;font-size:14.5px;font-weight:600;line-height:19.5px;letter-spacing:.4px;color:#333}
.share{left:910px;top:213px;font-size:13px;color:var(--link)}
.soc{position:absolute;top:208px;width:24px;height:22px;background:var(--icon)}
.rating{left:599px;top:259px;display:flex;gap:1px}
.reviews{left:682px;top:259px;font-size:10.5px;color:var(--link)}
.reviews .sep{color:#333}
.price{left:601px;top:288px;font-size:11px;color:var(--muted)}
.price b{font-size:14px;color:var(--red);font-weight:700;margin-left:4px;letter-spacing:.3px}
.ref{left:601px;top:311px;font-size:10px;color:var(--muted)}
.ref b{font-size:12px;font-weight:400;color:#333;margin-left:3px;letter-spacing:.4px}
.desc-label{left:600px;top:339px;font-size:13px;font-weight:600}
.desc{left:599px;top:358px;font-size:12.5px;line-height:16px;color:#444;width:470px}

.btn{position:absolute;top:541px;width:151px;height:33px;color:#fff;font-size:14.5px;font-weight:600;display:flex;align-items:center;justify-content:center;gap:8px;box-shadow:0 2px 3px rgba(0,0,0,.2)}
.btn.cart{left:606px;background:var(--orange)}
.btn.buy{left:768px;background:var(--brick)}

.similar-title{left:148px;top:680px;font-size:21px;font-weight:600;letter-spacing:.6px;color:#333}
.card{position:absolute;top:731px;width:157px;height:204px;background:var(--white);border:1px solid #dcdcdc;text-align:center}
.card .pic{height:119px;background:linear-gradient(160deg,#8a8a8a 0%,#c9c9c9 40%,#4a4140 100%)}
.card .pic.wood{background:linear-gradient(180deg,#3a3030 0%,#8a5a30 45%,#b07a44 70%,#2a2020 100%)}
.card .name{font-size:11px;font-weight:600;line-height:14.5px;margin-top:9px;padding:0 4px;height:29px;white-space:nowrap}
.card .cost{font-size:10.5px;color:var(--cyan);margin-top:4px}
.card .qty{font-size:10.5px;margin-top:5px}
</style>
</head>
<body>

<nav class="dept-nav">
  <div class="dept active" style="left:146px">Bar Furniture</div>
  <div class="dept" style="left:330px">Bar Equipment</div>
  <div class="dept" style="left:515px">Restaurant Furniture</div>
  <div class="dept" style="left:699px">Catering Equipment</div>
  <div class="dept" style="left:883px">Bedroom Furniture</div>
</nav>

<section class="product-panel"></section>

<nav class="sub-nav">
  <div class="sub active" style="left:164px">All</div>
  <div class="sub" style="left:220px">Bar Stools</div>
  <div class="sub" style="left:331px">Bar Tables</div>
  <div class="sub" style="left:443px">Benches</div>
  <div class="sub" style="left:555px">Tub chairs</div>
  <div class="sub" style="left:667px">Arm chairs</div>
  <div class="sub" style="left:779px">Pub Mirrors</div>
  <div class="sub" style="left:891px">Pub Signs</div>
</nav>

<div class="thumb current" style="top:216px"><span role="img" aria-label="Illuminated mobile bar, front view"></span></div>
<div class="thumb" style="top:267px"><span role="img" aria-label="Illuminated mobile bar, side view"></span></div>
<div class="thumb" style="top:317px"><span role="img" aria-label="Illuminated mobile bar, angled view"></span></div>
<div class="gallery-frame"></div>
<div class="gallery-photo" role="img" aria-label="Photo of a 2m mobile bar with a glowing red lightbox front panel"></div>

<h1 class="abs title">2m Mobile Bar. Large Lightbox Panel.<br>Good Used Condition - Bristol</h1>
<div class="abs share">Share</div>
<div class="soc" style="left:952px" aria-label="Share link"></div>
<div class="soc" style="left:981px" aria-label="Share link"></div>
<div class="soc" style="left:1010px" aria-label="Share link"></div>

<div class="abs rating" aria-label="4 out of 5 stars">
  <svg width="66" height="13" viewBox="0 0 66 13">
    <g fill="#b0333a">
      <polygon points="6.5,0.5 8.2,4.6 12.6,4.8 9.2,7.6 10.3,11.9 6.5,9.5 2.7,11.9 3.8,7.6 0.4,4.8 4.8,4.6"/>
      <polygon transform="translate(13,0)" points="6.5,0.5 8.2,4.6 12.6,4.8 9.2,7.6 10.3,11.9 6.5,9.5 2.7,11.9 3.8,7.6 0.4,4.8 4.8,4.6"/>
      <polygon transform="translate(26,0)" points="6.5,0.5 8.2,4.6 12.6,4.8 9.2,7.6 10.3,11.9 6.5,9.5 2.7,11.9 3.8,7.6 0.4,4.8 4.8,4.6"/>
      <polygon transform="translate(39,0)" points="6.5,0.5 8.2,4.6 12.6,4.8 9.2,7.6 10.3,11.9 6.5,9.5 2.7,11.9 3.8,7.6 0.4,4.8 4.8,4.6"/>
    </g>
    <polygon fill="#d0d0d0" transform="translate(52,0)" points="6.5,0.5 8.2,4.6 12.6,4.8 9.2,7.6 10.3,11.9 6.5,9.5 2.7,11.9 3.8,7.6 0.4,4.8 4.8,4.6"/>
  </svg>
</div>
<div class="abs reviews">1,178 customer reviews <span class="sep">&nbsp;|&nbsp;</span>7 answered questions</div>

<div class="abs price">Price: <b>£1000 VAT Free</b></div>
<div class="abs ref">Ref# : <b>C03A5D7D0A4C</b></div>

<div class="abs desc-label">Description:</div>
<p class="abs desc">2m mobile bar. Used for cocktail events.<br>
There are some marks on the top (can easily be polished off)<br>
Light panel has a few dents on the front. see pics. Works perfectly.<br>
One of the shelves is slightly bent. can still be used without any&nbsp; inconvenience.</p>

<div class="btn cart">
  <svg width="18" height="15" viewBox="0 0 18 15" fill="none" stroke="#fff" stroke-width="1.3"><path d="M1 1h3l2 9h9l2-6H5"/><circle cx="7" cy="13" r="1.2"/><circle cx="14" cy="13" r="1.2"/></svg>
  Add to Cart
</div>
<div class="btn buy">
  <svg width="15" height="17" viewBox="0 0 15 17" fill="none" stroke="#fff" stroke-width="1.2"><rect x="1" y="1" width="9" height="14"/><path d="M3 4h5M3 7h5M3 10h3"/><rect x="8" y="9" width="6" height="7"/></svg>
  Buy Now
</div>

<h2 class="abs similar-title">Similar Products</h2>

<div class="card" style="left:148px">
  <div class="pic" role="img" aria-label="Photo of a stainless steel bar top"></div>
  <div class="name">Collarless Quick Shot 3-ball<br>Pourers (327) - Somerset</div>
  <div class="cost">£1000 VAT Free</div>
  <div class="qty">Quantity: 21</div>
</div>
<div class="card" style="left:337px">
  <div class="pic" role="img" aria-label="Photo of a back-bar unit with shelves"></div>
  <div class="name">35ml Optics - Woking,<br>Surrey</div>
  <div class="cost">£2500 +VAT</div>
  <div class="qty">Quantity: 700</div>
</div>
<div class="card" style="left:526px">
  <div class="pic" role="img" aria-label="Photo of a steel bar counter"></div>
  <div class="name">Tavernline Wine Dispen-<br>sers WD24 - London</div>
  <div class="cost">£399 +VAT</div>
  <div class="qty">Quantity: 500</div>
</div>
<div class="card" style="left:714px">
  <div class="pic" role="img" aria-label="Photo of a bar unit with open shelving"></div>
  <div class="name">Steins - Job Lot -<br>London</div>
  <div class="cost">£1250 Including VAT</div>
  <div class="qty">Quantity: 223</div>
</div>
<div class="card" style="left:903px">
  <div class="pic wood" role="img" aria-label="Photo of a curved wooden pub bar"></div>
  <div class="name">New Tequila Shooter<br>25mls Glasses - London</div>
  <div class="cost">£10 +VAT</div>
  <div class="qty">Quantity: 100</div>
</div>

</body>
</html>
```